Bright Tooth Dentistry Business Card

We need business cards for our dental office.
We are looking for a clean, elegant design

We provide dental services to children.
Our card needs to be appealing to referring dentists, parents and our team

Target Market(s)

referring dentists, parents and our team

Industry/Entity Type

Dental Clinic

Contact Information for Business Card

4816 Juniper Lane, Suite 240
Fairhaven Hills, PA 15237

412-837-2961 Voice
412-837-2962 fax
info@brighttoothdentalpa.com email
www.brighttoothdentalpa.com web

Font styles to use
Sans Serif

Requirements
Must have
• White background - clean, crisp, elegant, simple
• rounded corners
• different color palate - once we come up with design, we will replace the blue with orange, green,
Nice to have
• Follow our logo typeface and colors
• then we can replace color

```html
<!DOCTYPE html>
<html lang="en">
<head>
<meta charset="utf-8">
<title>Bright Tooth Dentistry – Business Card</title>
<link rel="stylesheet" href="https://fonts.googleapis.com/css2?family=Quicksand:wght@600&family=Arimo:wght@400&display=swap">
<style>
  :root {
    --brand-blue: #00aeef;
    --band-gray: #a7a9ac;
    --text-gray: #4d4d4f;
    --card-white: #ffffff;
    --backdrop: #e8e4df;
  }
  * { margin: 0; padding: 0; box-sizing: border-box; }
  html, body { width: 1200px; height: 900px; overflow: hidden; }
  body { background: var(--backdrop); position: relative; font-family: "Arimo", Arial, sans-serif; }

  .card {
    position: absolute;
    width: 555px;
    height: 343px;
    box-shadow: 3px 4px 6px rgba(0,0,0,0.45);
    overflow: hidden;
  }
  .card--front { left: 330px; top: 90px; background: var(--card-white); }
  .card--back { left: 330px; top: 470px; width: 558px; background: var(--brand-blue); }

  .brand-name {
    position: absolute;
    font-family: "Quicksand", "Arimo", sans-serif;
    font-weight: 600;
    white-space: nowrap;
  }
  .card--front .brand-name {
    right: 30px; top: 122px;
    font-size: 31px;
    color: var(--brand-blue);
  }
  .brand-dot {
    position: absolute;
    border-radius: 50%;
  }
  .card--front .brand-dot {
    right: 30px; top: 58px;
    width: 46px; height: 46px;
    background: var(--brand-blue);
  }

  .contact-list {
    position: absolute;
    left: 25px; top: 229px;
    list-style: none;
    font-size: 16px;
    line-height: 20.5px;
    color: var(--text-gray);
  }
  .contact-list li { display: flex; align-items: center; }
  .contact-icon { width: 15px; height: 13px; margin-right: 7px; fill: var(--brand-blue); }

  .address {
    position: absolute;
    right: 30px; top: 229px;
    text-align: right;
    font-style: normal;
    font-size: 16px;
    line-height: 20.5px;
    color: var(--text-gray);
  }

  .footer-bands { position: absolute; left: 0; bottom: 0; width: 555px; height: 32px; }
  .web-front {
    position: absolute;
    right: 31px; bottom: 9px;
    font-size: 15px;
    color: var(--card-white);
  }

  .card--back .brand-dot {
    left: 254px; top: 100px;
    width: 50px; height: 50px;
    background: var(--card-white);
  }
  .card--back .brand-name {
    left: 0; width: 100%; top: 168px;
    text-align: center;
    font-size: 30px;
    color: var(--card-white);
  }
  .web-back {
    position: absolute;
    left: 0; width: 100%; top: 278px;
    text-align: center;
    font-size: 15px;
    color: var(--card-white);
  }
</style>
</head>
<body>

<section class="card card--front" aria-label="Business card front">
  <span class="brand-dot" aria-hidden="true"></span>
  <h1 class="brand-name">Bright Tooth Dentistry</h1>

  <ul class="contact-list">
    <li>
      <svg class="contact-icon" viewBox="0 0 16 14" aria-hidden="true">
        <path d="M1 4.5C1 2 4 1 8 1s7 1 7 3.5v1h-3.5V4H4.5v1.5H1z"/>
        <path d="M4 6h8l2 5v2H2v-2z"/>
      </svg>412-837-2961
    </li>
    <li>
      <svg class="contact-icon" viewBox="0 0 16 14" aria-hidden="true">
        <rect x="4" y="0.5" width="8" height="4"/>
        <path d="M1 5h14v6h-2.5V9h-9v2H1z"/>
        <rect x="4.5" y="10" width="7" height="4"/>
      </svg>412-837-2962
    </li>
    <li>
      <svg class="contact-icon" viewBox="0 0 16 12" aria-hidden="true">
        <path d="M1 1h14v10H1zM2.5 2.5v.6L8 7l5.5-3.9v-.6zM2.5 4.8v4.7h11V4.8L8 8.7z" fill-rule="evenodd"/>
      </svg>info@brighttoothdentalpa.com
    </li>
  </ul>

  <address class="address">
    4816 Juniper Lane, Suite 240<br>
    Fairhaven Hills<br>
    PA 15237
  </address>

  <svg class="footer-bands" viewBox="0 0 555 32" aria-hidden="true">
    <polygon points="0,7 275,7 268,19 0,19" fill="var(--band-gray)"/>
    <polygon points="282,0 555,0 555,32 262,32" fill="var(--brand-blue)"/>
    <rect x="0" y="24" width="270" height="8" fill="var(--brand-blue)"/>
  </svg>
  <span class="web-front">www.brighttoothdentalpa.com</span>
</section>

<section class="card card--back" aria-label="Business card back">
  <span class="brand-dot" aria-hidden="true"></span>
  <h2 class="brand-name">Bright Tooth Dentistry</h2>
  <span class="web-back">www.brighttoothdentalpa.com</span>
</section>

</body>
</html>
```